UPDATE: Web Page: Meridew Public Relations

i DON'T NEED PICTURES, JUST SOMETHING CLEAN LIKE THE ARTWORK ATTACHED OR BUILT ON BUSINESS CARDS...PLEASE DESIGN AROUND THAT.

I need a clean webpage for new public relations firm that I will launch on March 1st. I HAVE JUST ADDED BUSINESS CARD MODELS FOR WEB PAGE COVER AND START IN TERMS OF DESIGN.

Pull down categories: (built on this model: http://www.quornsvalepr.com/contact/)

-Home
-Services
-Expertise
-About Us
-Press
-Contact

Garth Pelliam, CEO
Meridew Public Relations
2875 West Hallowmere Blvd.
Los Angeles CA 90047
(o) 213.555.0148
(f) 213.555.0193
garth@meridewmpr.com

Target Market(s)

Varnholt Civic Assembly, Orvane Civic Hall
Lobbying type services to government/public affairs

Industry/Entity Type

Business

Number of Pages Required

4 page

Requirements
Must have
• Portray a beautiful picture of LA City or a government hall way (not domes)
• 1. Public Relations---Pic of Advocacy
• 2. Public Affairs--pick of government capitol Sacramento/Orvane Civic Hall
• 3. Strategy & Advisory Services--Something smart like chalk board.
Nice to have
• Great Pics on slider pages
Should not have
• Varnholt Assembly Dome
• Orvane Civic Hall

```html
<!DOCTYPE html>
<html lang="en">
<head>
<meta charset="utf-8">
<title>Meridew Public Relations</title>
<link href="https://fonts.googleapis.com/css2?family=Open+Sans:wght@400;600;700&display=swap" rel="stylesheet">
<style>
  :root {
    --blue: #1f6fc2;
    --blue-dark: #0c4f98;
    --blue-light: #3a8ad8;
    --ink: #2d2d2d;
    --muted: #777;
    --line: #e2e2e2;
    --card: #f3f3f3;
    --footer: #2c2c2c;
    --footer-base: #1f1f1f;
    --footer-text: #a9a9a9;
    --white: #fff;
  }
  * { box-sizing: border-box; margin: 0; padding: 0; }
  html, body { width: 829px; height: 1200px; overflow: hidden; }
  body { font-family: "Open Sans", Arial, sans-serif; color: var(--ink); background: var(--white); position: relative; }

  .site-header { height: 78px; display: flex; align-items: center; justify-content: space-between; padding: 0 68px 0 96px; }
  .brand { display: flex; align-items: center; gap: 8px; }
  .brand-dot { width: 30px; height: 30px; border-radius: 50%; background: var(--blue); }
  .brand-name { font-size: 22px; font-weight: 700; color: var(--blue); }
  .main-nav { display: flex; gap: 4px; }
  .main-nav a { font-size: 10px; color: var(--ink); text-decoration: none; padding: 8px 12px; }
  .main-nav a.active { background: var(--blue); color: var(--white); }

  .hero { height: 248px; background: linear-gradient(180deg, var(--blue-light), var(--blue-dark)); position: relative; box-shadow: 0 6px 10px rgba(0,0,0,.15); }
  .hero-copy { position: absolute; left: 138px; top: 62px; width: 250px; color: var(--white); }
  .hero-title { font-size: 24px; font-weight: 400; line-height: 1.15; }
  .hero-sub { font-size: 13px; margin: 4px 0 10px; }
  .hero-text { font-size: 7px; line-height: 1.5; opacity: .85; }
  .btn { display: inline-block; background: #1d1d1d; color: var(--white); font-size: 8px; padding: 6px 14px; text-decoration: none; }
  .hero .btn { margin-top: 14px; }
  .hero-dots { display: flex; gap: 5px; margin-top: 12px; }
  .hero-dots span { width: 7px; height: 7px; border-radius: 50%; background: rgba(255,255,255,.5); }
  .hero-dots span:first-child { background: var(--white); }
  .hero-art { position: absolute; left: 430px; top: 0; }

  .intro { text-align: center; width: 560px; margin: 44px auto 0; }
  .intro h1 { font-size: 19px; font-weight: 400; }
  .intro .lead { font-size: 10px; color: var(--muted); margin-top: 4px; }
  .intro p.body { font-size: 7px; color: var(--muted); line-height: 1.6; margin-top: 10px; }

  .services { display: flex; gap: 14px; width: 546px; margin: 50px auto 0; }
  .service-card { flex: 1; background: var(--card); border: 1px solid var(--line); text-align: center; padding-bottom: 12px; }
  .service-photo { height: 92px; }
  .service-card h2 { font-size: 15px; font-weight: 400; color: var(--blue); margin: 10px 0 4px; }
  .service-card p { font-size: 6.5px; color: var(--muted); line-height: 1.5; padding: 0 10px; }
  .service-card .btn { background: var(--blue-dark); margin-top: 8px; }

  .latest { display: flex; gap: 20px; width: 546px; margin: 36px auto 0; }
  .latest h3 { font-size: 10px; font-weight: 700; text-transform: uppercase; margin-bottom: 10px; }
  .blogs { flex: 2; }
  .projects { flex: 1.05; }
  .projects h3 { color: var(--blue); }
  .post { display: flex; gap: 10px; margin-bottom: 10px; }
  .post-thumb { width: 60px; height: 56px; flex: none; }
  .post h4, .project h4 { font-size: 7px; font-weight: 600; color: var(--blue); }
  .post p, .project p { font-size: 6px; color: var(--muted); line-height: 1.5; }
  .post .more { font-size: 6px; color: var(--blue); }
  .project { margin-bottom: 8px; }
  .project-feature { display: flex; gap: 6px; }
  .project-thumb { width: 44px; height: 42px; flex: none; }

  .site-footer { position: absolute; left: 0; bottom: 0; width: 829px; height: 184px; background: var(--footer); }
  .footer-cols { display: flex; width: 560px; margin: 22px auto 0; gap: 24px; }
  .footer-col { flex: 1; }
  .footer-col h5 { font-size: 8px; color: var(--white); font-weight: 700; margin-bottom: 6px; text-transform: uppercase; }
  .footer-col li { list-style: none; font-size: 6.5px; color: var(--footer-text); line-height: 1.7; }
  .footer-col p { font-size: 6.5px; color: var(--footer-text); }
  .social { display: flex; gap: 4px; margin: 6px 0 12px; }
  .social span { width: 13px; height: 13px; background: #555; border-radius: 2px; }
  .footer-brand { display: flex; align-items: center; gap: 6px; }
  .footer-brand .brand-dot { width: 22px; height: 22px; background: var(--white); }
  .footer-brand .brand-name { font-size: 17px; color: var(--white); }
  .footer-base { position: absolute; bottom: 0; left: 0; width: 100%; height: 26px; background: var(--footer-base); font-size: 6px; color: #888; padding: 9px 0 0 96px; }
</style>
</head>
<body>
  <header class="site-header">
    <div class="brand"><span class="brand-dot"></span><span class="brand-name">Meridew</span></div>
    <nav class="main-nav">
      <a class="active" href="#">Home</a><a href="#">Services</a><a href="#">Expertise</a><a href="#">About Us</a><a href="#">Press</a><a href="#">Contact</a>
    </nav>
  </header>

  <section class="hero">
    <div class="hero-copy">
      <h2 class="hero-title">Public Relation Services</h2>
      <p class="hero-sub">Etiam est nunc venenatis in tristique eu</p>
      <p class="hero-text">Nulla facilisi, integer sed nunc at lorem pretium facilisis. Donec vel neque quis odio tincidunt porta. Sed varius mauris eget dolor luctus, nec tempor magna aliquet.</p>
      <a class="btn" href="#">Read More</a>
      <div class="hero-dots"><span></span><span></span><span></span></div>
    </div>
    <svg class="hero-art" width="330" height="248" viewBox="0 0 330 248">
      <defs>
        <radialGradient id="photoA" cx="50%" cy="45%" r="60%"><stop offset="0" stop-color="#7cc3ee"/><stop offset="1" stop-color="#1b4f8e"/></radialGradient>
        <linearGradient id="photoB" x1="0" y1="0" x2="1" y2="1"><stop offset="0" stop-color="#d9dde2"/><stop offset="1" stop-color="#8a97a6"/></linearGradient>
      </defs>
      <g role="img" aria-label="Photo of a city skyline with a digital network overlay">
        <circle cx="136" cy="118" r="118" fill="url(#photoA)" stroke="#fff" stroke-width="4"/>
      </g>
      <g role="img" aria-label="Small photos of people at work in an office">
        <circle cx="272" cy="52" r="26" fill="url(#photoB)" stroke="#fff" stroke-width="3"/>
        <circle cx="294" cy="104" r="22" fill="url(#photoB)" stroke="#fff" stroke-width="3"/>
        <circle cx="282" cy="152" r="20" fill="url(#photoB)" stroke="#fff" stroke-width="3"/>
        <circle cx="258" cy="202" r="24" fill="url(#photoB)" stroke="#fff" stroke-width="3"/>
      </g>
    </svg>
  </section>

  <section class="intro">
    <h1>Mauris vel lacus vitae felis vestibulum volutpat</h1>
    <p class="lead">Lorem ipsum dolor sit amet consectetuer adipiscing elit nunc cursus</p>
    <p class="body">Quisque placerat nunc sed ultricies tristique, donec semper sapien eu pretium convallis. Pellentesque habitant morbi tristique senectus et netus et malesuada fames ac turpis egestas. Vivamus rutrum justo at nibh aliquet, vel feugiat lorem dictum. Aenean sodales metus non erat laoreet, sit amet gravida arcu tempus. Curabitur eget mi vitae purus finibus posuere.</p>
  </section>

  <section class="services">
    <article class="service-card">
      <div class="service-photo" role="img" aria-label="Photo of a woman speaking on the phone at a desk" style="background:linear-gradient(135deg,#c9b7a4,#6f5f52)"></div>
      <h2>Public Relations</h2>
      <p>Morbi tempus lectus nec magna ornare, vitae pulvinar tortor aliquam. Sed id lacus eu risus varius.</p>
      <a class="btn" href="#">Read More</a>
    </article>
    <article class="service-card">
      <div class="service-photo" role="img" aria-label="Photo of a marketing strategy board with charts" style="background:linear-gradient(135deg,#e6e8ea,#8f9aa5)"></div>
      <h2>Marketing Service</h2>
      <p>Phasellus luctus arcu sed nisl feugiat, in posuere elit congue. Nam auctor diam vel sem faucibus.</p>
      <a class="btn" href="#">Read More</a>
    </article>
    <article class="service-card">
      <div class="service-photo" role="img" aria-label="Illustration of social media network icons" style="background:linear-gradient(135deg,#8fc9f0,#2b6fb5)"></div>
      <h2>Social Media</h2>
      <p>Integer gravida turpis at erat mollis, nec dapibus nunc tincidunt. Cras blandit velit in urna tempor.</p>
      <a class="btn" href="#">Read More</a>
    </article>
  </section>

  <section class="latest">
    <div class="blogs">
      <h3>Latest Blogs</h3>
      <div class="post">
        <div class="post-thumb" role="img" aria-label="Photo of hands typing on a laptop" style="background:linear-gradient(135deg,#4b5f7a,#18243a)"></div>
        <div>
          <h4>Cum sociis natoque</h4>
          <p>Aliquam erat volutpat, donec finibus velit quis lorem vehicula, ac iaculis magna posuere. Suspendisse potenti, nunc vel libero sed tortor imperdiet tempus.</p>
          <span class="more">Read More</span>
        </div>
      </div>
      <div class="post">
        <div class="post-thumb" role="img" aria-label="Photo of a business meeting around a table" style="background:linear-gradient(135deg,#aeb6c0,#4d5866)"></div>
        <div>
          <h4>Cum sociis natoque</h4>
          <p>Vestibulum ante ipsum primis in faucibus orci luctus et ultrices, sed mattis neque in augue porta. Fusce dictum arcu vel justo blandit viverra.</p>
          <span class="more">Read More</span>
        </div>
      </div>
    </div>
    <div class="projects">
      <h3>Latest Projects</h3>
      <div class="project project-feature">
        <div class="project-thumb" role="img" aria-label="Photo of a woman smiling in an office" style="background:linear-gradient(135deg,#d8c4b0,#8a7360)"></div>
        <div>
          <h4>Lorem ipsum dolor</h4>
          <p>Donec ut nisl vel augue ornare tempus id at purus.</p>
        </div>
      </div>
      <div class="project">
        <h4>Morbi diam lacus gravida</h4>
        <p>Nullam quis metus eget arcu semper pulvinar, ut rhoncus leo elementum sed.</p>
      </div>
      <div class="project">
        <h4>Cum sociis natoque</h4>
        <p>Etiam pretium massa eu mauris cursus lobortis in eget nisi.</p>
      </div>
    </div>
  </section>

  <footer class="site-footer">
    <div class="footer-cols">
      <div class="footer-col">
        <h5>Company</h5>
        <ul><li>About Company</li><li>What We Do</li><li>Testimonials</li><li>Blog Post</li></ul>
      </div>
      <div class="footer-col">
        <h5>Services</h5>
        <ul><li>Public Relations</li><li>Social Media Management</li><li>Marketing Service</li><li>Public Services</li><li>Client and Affairs</li></ul>
      </div>
      <div class="footer-col">
        <h5>Support</h5>
        <ul><li>Contact Us</li><li>Terms of Use</li><li>Sitemap</li></ul>
      </div>
      <div class="footer-col">
        <h5>Get in Touch</h5>
        <p>Please connect with us here</p>
        <div class="social"><span></span><span></span><span></span></div>
        <div class="footer-brand"><span class="brand-dot"></span><span class="brand-name">Meridew</span></div>
      </div>
    </div>
    <div class="footer-base">© 2014 Meridew PR. All rights reserved.</div>
  </footer>
</body>
</html>
```